Brisco Skiff Ferry and Haulage Business Card

I need business cards for my new water taxi and freight transport business I have started here in Kodiak Alaska. Kodiak is a remote island in the middle of the gulf of Alaska. There are seven native villages around the island and Kodiak is the #2 fishing port in the United States. We also have the largest Harbor Watch Base in the U.S. My company will be providing water taxi and freight transport logistics to the villages and many hunting and fishing lodges as well as remote properties around the island.

I would like a business card that isn't status quo, something that stands out, either in feel or appearance. I do like clean minimal designs but it needs to have the necessary contact info on it.

Target Market(s)

remote lodge / property owners, residents of the many villages around Kodiak and any one wanting to enjoy the great outdoors of Kodiak Alaska

Industry/Entity Type

Business

Contact Information for Business Card

I like clean simple designs that aren't cluttered but still provide the necessary information

Colors
0255a3
3277b5
33a4d5
9bcb3c
add136
fbed22
ffc214
f78f20
f37122

Requirements
Must have
• logo and contact info
• Captain Wade Pemberton
• www.briscoskiffferry.net
• wade@briscoskiffferry.net

```html
<!DOCTYPE html>
<html lang="en">
<head>
<meta charset="utf-8">
<title>Brisco Skiff Ferry and Haulage – Business Card</title>
<link href="https://fonts.googleapis.com/css2?family=Questrial&display=swap" rel="stylesheet">
<style>
  :root{
    --navy:#0255a3;
    --blue:#3277b5;
    --sky:#33a4d5;
    --orange:#f78f20;
    --amber:#ffc214;
    --ink:#5f6670;
    --paper:#ffffff;
    --backdrop:#e9e7e3;
    --sea-deep:#0f3f86;
    --sea-mid:#2a72c4;
    --sky-light:#a9cdf0;
  }
  *{box-sizing:border-box;margin:0;padding:0}
  html,body{width:1200px;height:950px;overflow:hidden}
  body{background:var(--backdrop);font-family:"Questrial",sans-serif;position:relative}
  .card{position:absolute;left:250px;width:700px;height:400px;border-radius:4px;overflow:hidden;box-shadow:0 8px 24px rgba(0,0,0,.18)}
  .card--front{top:55px}
  .card--back{top:495px;background:var(--paper)}

  .front-photo{position:absolute;inset:0;background:linear-gradient(170deg,var(--sky-light) 0%,#7fb2e4 22%,var(--sea-mid) 40%,var(--sea-deep) 75%,#0b2f6a 100%)}
  .front-brand{position:absolute;left:150px;top:215px;display:flex;flex-direction:column;align-items:center;color:#fff}
  .front-brand .mark-dot{width:54px;height:54px;border-radius:50%;border:3px solid #fff;margin-bottom:12px}
  .front-brand .brand-name{font-size:26px;line-height:1.15;text-align:center;color:#fff}
  .social-row{display:flex;gap:10px;margin-top:14px}
  .social-row span{width:22px;height:22px;border-radius:50%;background:#fff}

  .back-logo{position:absolute;left:40px;top:120px;width:260px;display:flex;flex-direction:column;align-items:center}
  .back-logo .mark-dot{width:64px;height:64px;border-radius:50%;background:var(--sky);margin-bottom:16px}
  .back-logo .brand-name{font-size:28px;line-height:1.15;color:var(--navy);text-align:center}
  .divider{position:absolute;left:330px;top:60px;width:1px;height:200px;background:#d6d9de}
  .contact{position:absolute;left:360px;top:62px;color:var(--ink)}
  .contact .name{font-size:22px;letter-spacing:.5px;color:var(--blue);font-weight:700}
  .contact .role{font-size:17px;color:var(--orange);margin:3px 0 8px}
  .contact .addr{font-size:15px;line-height:1.35}
  .contact ul{list-style:none;margin-top:8px}
  .contact li{font-size:15px;line-height:1.55;display:flex;align-items:center;gap:9px}
  .contact li svg{width:13px;height:13px;flex:none;fill:var(--navy)}
  .swoosh{position:absolute;left:0;bottom:0;width:700px;height:240px}
</style>
</head>
<body>

<section class="card card--front">
  <div class="front-photo" role="img" aria-label="Photo of a water taxi boat cruising across a blue bay with snowy mountains and sky"></div>
  <div class="front-brand">
    <span class="mark-dot"></span>
    <p class="brand-name">Brisco Skiff Ferry<br>and Haulage</p>
    <div class="social-row"><span></span><span></span><span></span></div>
  </div>
</section>

<section class="card card--back">
  <div class="back-logo">
    <span class="mark-dot"></span>
    <p class="brand-name">Brisco Skiff Ferry<br>and Haulage</p>
  </div>
  <div class="divider"></div>
  <div class="contact">
    <p class="name">WADE PEMBERTON</p>
    <p class="role">Captain</p>
    <p class="addr">214 Tidewater Row<br>Anchorage, Alaska 99517</p>
    <ul>
      <li><svg viewBox="0 0 16 16"><path d="M3.6 1.2l2.3 2.7-1.4 1.6c.9 2.1 2.4 3.7 4.6 4.7l1.6-1.4 2.7 2.3-1.3 2.6C6.6 13.4 2.6 9.4 1 3.9z"/></svg>907 555 0148</li>
      <li><svg viewBox="0 0 16 16"><path d="M1 3h14v10H1zM2.3 4.2 8 8.6l5.7-4.4z"/></svg>wade@briscoskiffferry.net</li>
      <li><svg viewBox="0 0 16 16"><circle cx="8" cy="8" r="7"/></svg>www.briscoskiffferry.net</li>
    </ul>
  </div>
  <svg class="swoosh" viewBox="0 0 700 240" preserveAspectRatio="none">
    <path d="M0 240 L0 215 C180 240 380 215 520 130 C600 80 660 40 700 20 L700 240 Z" fill="var(--navy)"/>
    <path d="M0 232 C180 250 390 225 525 145 C605 95 660 60 700 40 L700 60 C655 82 605 115 530 160 C395 240 190 262 0 240 Z" fill="var(--paper)"/>
    <path d="M0 200 C200 225 390 200 520 115 C600 65 660 30 700 12 L700 22 C660 40 605 75 525 125 C395 212 200 238 0 212 Z" fill="var(--orange)"/>
  </svg>
</section>

</body>
</html>
```